One-Page Flat Design for SEO Company [2 DAYS]

We need a one-page flat design for our SEO company. Our current website is http://www.rankloft.com/. We are looking to completely re-design the site using new flat design techniques.
Below are some examples of the type of style we're going after:
http://quormel.com/
http://tobyrand.co.uk/
https://pentaly.co/
http://milesporter.me/
As you can see- flat, clean, minimal. It is very important you follow this type of style.
For colour scheme, you may use one of the pre-made colour palettes from here:
http://www.vornacle.com/blog/inspiration/24-flat-designs-with-compelling-color-palettes
I've attached a wireframe to be followed.
Hi,

```html
<!DOCTYPE html>
<html lang="en">
<head>
<meta charset="utf-8">
<title>RankLoft — One-Page SEO</title>
<link href="https://fonts.googleapis.com/css2?family=Open+Sans:ital,wght@0,400;0,600;0,700;1,400&family=Archivo+Black&display=swap" rel="stylesheet">
<style>
:root{
  --orange:#f26b1d;
  --orange-dark:#d9560c;
  --green:#6cbf3a;
  --green-dark:#55a52a;
  --ink:#222;
  --text:#555;
  --muted:#999;
  --line:#e3e3e3;
  --panel:#f3f3f3;
  --footer:#ececec;
  --white:#fff;
  --cream:#f8f6ee;
}
*{box-sizing:border-box;margin:0;padding:0}
html,body{width:1200px;height:2675px;overflow:hidden;background:var(--white)}
body{position:relative;font-family:"Open Sans",Arial,sans-serif;color:var(--text);font-size:12.5px;line-height:1.6}
.abs{position:absolute}

/* header */
.brand{left:149px;top:22px;display:flex;align-items:center;gap:10px}
.brand-mark{width:30px;height:30px;border-radius:50%;background:var(--orange)}
.brand-name{font-size:34px;font-weight:700;color:var(--orange);letter-spacing:-.5px}
.social{display:flex;gap:14px}
.social span{width:14px;height:14px;border-radius:50%;background:#b8b8b8;display:block}
.header-social{left:841px;top:44px}
.header-rule{left:0;top:118px;width:1200px;height:2px;background:var(--orange)}

/* nav */
.nav{left:149px;top:120px;height:71px;display:flex}
.nav-item{padding:18px 22px 0 18px;border-right:1px solid var(--line);height:48px;margin-top:12px;padding-top:4px}
.nav-item:last-child{border-right:0}
.nav-item b{display:block;font-weight:400;font-size:16px;color:#888;line-height:1.2}
.nav-item small{display:block;font-size:9px;color:var(--muted)}
.nav-item.active b{color:var(--orange)}
.nav-active-bar{left:149px;top:188px;width:90px;height:3px;background:var(--orange)}
.search-panel{left:869px;top:122px;width:182px;height:69px;background:var(--panel)}
.search{left:881px;top:144px;width:157px;height:26px;border:1px solid #ccc;background:var(--white);font-size:11px;color:var(--muted);padding:4px 8px}
.search i{position:absolute;right:0;top:0;width:24px;height:24px;border-left:1px solid #ccc}

/* hero */
.hero{left:0;top:191px;width:1200px;height:424px;background:linear-gradient(90deg,#f1f1f1,#f7f7f7 55%,#fbfbfb)}
.hero-art{left:506px;top:191px;width:545px;height:424px;background:radial-gradient(ellipse at 55% 55%,#ffffff 0%,#f0f0f0 45%,#f7f7f7 75%)}
.hero-title{left:149px;top:336px;font-size:35px;color:var(--ink);font-weight:400;line-height:1.2}
.hero-sub{left:149px;top:382px;font-size:23px;color:var(--orange);line-height:1.2}
.hero-copy{left:149px;top:432px;width:330px;font-size:12px;line-height:1.55;color:#444}
.btn{background:var(--orange);color:var(--white);font-size:11.5px;border-radius:3px;text-align:center;line-height:23px;height:23px}
.hero-btn{left:149px;top:499px;width:86px}
.ctrl{width:30px;height:30px;border-radius:50%;border:1.5px solid #bbb;background:var(--white)}
.dot{width:10px;height:10px;border-radius:50%;border:1px solid #bbb}
.up{width:32px;height:32px;border-radius:50%;border:1.5px solid #bbb}

/* sections */
.sec-title{font-size:16px;color:var(--orange);line-height:1}
.sec-rule{height:1px;background:var(--line)}
.about-copy{left:149px;top:718px;width:902px;font-size:12px;line-height:1.55;color:#444}
.about-copy p+p{margin-top:12px}
.svc-arrows{left:1018px;top:882px;display:flex;gap:4px}
.svc-arrows span{width:15px;height:15px;border:1px solid #ccc;display:block}
.svc{width:285px}
.svc-art{width:112px;height:112px}
.svc h3{font-size:20px;font-weight:400;color:var(--orange);margin-top:12px;line-height:1.2}
.svc p{font-size:12px;line-height:1.5;margin-top:6px;color:#444}

/* plans */
.box{left:149px;width:902px;background:var(--panel);border-top:2px solid var(--orange)}
.plan{width:199px;background:var(--white);top:1336px;height:537px;box-shadow:0 1px 2px rgba(0,0,0,.08)}
.plan-head{height:68px;text-align:center;color:var(--white)}
.plan-head h4{font-family:"Archivo Black",Arial,sans-serif;font-weight:400;font-size:21px;letter-spacing:1px;color:#333;padding-top:10px;line-height:1.2}
.plan-head em{font-family:Georgia,serif;font-size:12px}
.plan.green .plan-head{background:var(--green)}
.plan.orange .plan-head{background:var(--orange)}
.plan-price{height:106px;background:var(--cream);position:relative;border-bottom:1px dashed #ddd}
.plan-price .amt{position:absolute;left:54px;top:26px;font-size:50px;font-weight:700;color:#222;line-height:1}
.plan-price .amt sup{font-size:24px;vertical-align:top;position:relative;top:6px}
.plan-price .join{position:absolute;right:0;top:37px;width:60px;height:28px;line-height:28px;font-size:10px;font-weight:700;color:var(--white);text-align:center;clip-path:polygon(12% 0,100% 0,100% 100%,12% 100%,0 50%)}
.plan.green .join{background:var(--green-dark)}
.plan.orange .join{background:var(--orange-dark)}
.plan ul{list-style:none;margin:10px 20px 0}
.plan li{font-size:9.5px;border-bottom:1px solid #eee;padding:7px 0 7px 16px;line-height:1.7;color:#555}
.plan .note{font-size:9.5px;text-align:center;padding:12px 20px 0;line-height:1.7;color:#555}

/* contact */
.label{font-size:11.5px;color:var(--muted)}
.label i{color:var(--orange);font-style:normal}
.field{background:var(--white);border:1px solid #bbb;border-radius:2px}

/* footer */
.footer{left:0;top:2366px;width:1200px;height:267px;background:var(--footer)}
.footer-brand{left:149px;top:2366px;width:210px;height:233px;background:var(--orange);color:var(--white);padding:28px 18px}
.footer-brand .name{font-size:28px;font-weight:700;color:var(--white);line-height:1.2}
.footer-brand .tag{font-size:14px;margin-top:4px}
.footer-brand p{font-size:12px;margin-top:38px;line-height:1.55}
.fcol{top:2402px;width:200px;font-size:11.5px;line-height:1.55;color:#444}
.fcol h5{font-size:14px;font-weight:400;color:var(--orange);margin-bottom:14px}
.fcol a{color:var(--orange);text-decoration:none}
.sub{margin-top:14px;display:flex;width:200px;height:24px;border:1px solid #ccc;background:var(--white);font-size:10px;color:var(--muted)}
.sub span{flex:1;padding:3px 6px}
.sub b{width:26px;border-left:1px solid #ccc;text-align:center;font-weight:400;line-height:22px}
.fine{font-size:9.5px;color:var(--muted);margin-top:6px;line-height:1.5}
.video{width:212px;height:120px;background:#dcdcdc}
.bottom{top:2633px;left:149px;width:902px;height:42px;font-size:10.5px;color:#777;display:flex;align-items:center}
</style>
</head>
<body>

<!-- header -->
<div class="abs brand"><span class="brand-mark"></span><span class="brand-name">RankLoft</span></div>
<div class="abs social header-social"><span></span><span></span><span></span><span></span><span></span><span></span><span></span><span></span></div>
<div class="abs header-rule"></div>

<!-- nav -->
<nav class="abs nav">
  <div class="nav-item active"><b>HOME</b><small>slogan here</small></div>
  <div class="nav-item"><b>ABOUT US</b><small>slogan here</small></div>
  <div class="nav-item"><b>OUR SERVICES</b><small>slogan here</small></div>
  <div class="nav-item"><b>FAQ</b><small>slogan here</small></div>
  <div class="nav-item" style="padding-left:40px"><b>CONTACT</b><small>slogan here</small></div>
</nav>
<div class="abs nav-active-bar"></div>
<div class="abs search-panel"></div>
<div class="abs search">Search...<i></i></div>

<!-- hero -->
<section class="abs hero"></section>
<div class="abs hero-art" role="img" aria-label="Two white dice with red pips tumbling"></div>
<h1 class="abs hero-title">Welcome to Company</h1>
<h2 class="abs hero-sub" style="font-weight:400">Lorem Ipsum Dolora</h2>
<p class="abs hero-copy">Sed ut cetero prompta sententiae. Vocibus electram te mei, eum eu nibh virtute, justo delenit albucius ea nec. Usu ne noster cetero epicurei.</p>
<div class="abs btn hero-btn">View details</div>
<div class="abs ctrl" style="left:1141px;top:367px"></div>
<div class="abs ctrl" style="left:1141px;top:421px"></div>
<div class="abs ctrl" style="left:1141px;top:476px"></div>
<div class="abs dot" style="left:1152px;top:540px"></div>
<div class="abs dot" style="left:1152px;top:560px"></div>
<div class="abs dot" style="left:1152px;top:580px"></div>
<div class="abs dot" style="left:1152px;top:599px"></div>

<!-- about -->
<h2 class="abs sec-title" style="left:149px;top:670px;font-weight:400">About Us</h2>
<div class="abs sec-rule" style="left:149px;top:703px;width:902px"></div>
<div class="abs about-copy">
  <p>Why spend countless hours trying to increase your search engine rankings? At RankLoft.com, we know how important backlinks are to your website which is why we offer affordable and professional SEO backlink services. The sheer power of our backlinks can quickly get your site ranking in a short amount of time. Stop wasting time on other providers and doing it yourself. We offer the best prices with REAL results.</p>
  <p>Our company prides itself in keeping the prices low for whatever it takes. You will be pleasantly surprised by our costs. Our methods are completely safe and risk-free. We provide all services manually and no 'black hat' techniques are involved. Our priority is quality and customer satisfaction. By working with us, you can be sure you'll receive top quality service.</p>
</div>
<div class="abs up" style="left:1143px;top:752px;opacity:.4"></div>

<!-- services -->
<h2 class="abs sec-title" style="left:149px;top:880px;font-weight:400">Our Services</h2>
<div class="abs svc-arrows"><span></span><span></span></div>
<div class="abs sec-rule" style="left:149px;top:905px;width:902px"></div>
<div class="abs up" style="left:1143px;top:878px"></div>
<div class="abs svc" style="left:149px;top:946px">
  <div class="svc-art" role="img" aria-label="Blue coin with a dollar sign" style="border-radius:50%;background:radial-gradient(circle at 40% 35%,#a9cbe8,#5a8fc4)"></div>
  <h3>Low Prices</h3>
  <p>Our company prides itself in keeping the prices low for whatever it takes. You will be pleasantly surprised by our costs.</p>
</div>
<div class="abs svc" style="left:455px;top:946px">
  <div class="svc-art" role="img" aria-label="Rising blue bar chart with a green arrow" style="background:linear-gradient(160deg,#8fd14f 0%,#5aa83a 35%,#2f86b8 60%,#1d6c9c 100%);border-radius:8px"></div>
  <h3>Increased Ranking</h3>
  <p>The sheer power of our backlinks can quickly get your site ranking in a short amount of time. Stop wasting time on other providers and doing it yourself. We offer the best prices with REAL results.</p>
</div>
<div class="abs svc" style="left:762px;top:946px">
  <div class="svc-art" role="img" aria-label="Grey database stack with a magnifying glass" style="background:linear-gradient(180deg,#f2f2f2,#bdbdbd);border-radius:18px"></div>
  <h3>High Quality Services</h3>
  <p>Our priority is quality and customer satisfaction. By working with us, you can be sure you'll receive top quality service.</p>
</div>

<!-- plans -->
<section class="abs box" style="top:1244px;height:659px"></section>
<h2 class="abs sec-title" style="left:199px;top:1286px;font-weight:400">Our Plan</h2>
<div class="abs sec-rule" style="left:199px;top:1318px;width:852px;background:#e6e6e6"></div>
<div class="abs up" style="left:1143px;top:1517px"></div>

<div class="abs plan green" style="left:216px">
  <div class="plan-head"><h4>BRONZE</h4><em>Great for small business</em></div>
  <div class="plan-price"><span class="amt"><sup>$</sup>39</span><span class="join">JOIN</span></div>
  <ul>
    <li>10 PR3 - PR8 Social Bookmarks</li>
    <li>15 PR5 - PR8 Web 2.0 Profile Backlinks</li>
    <li>100 .EDU Backlinks</li>
    <li>150 PR5 - PR7 Backlinks</li>
    <li>One-Way Links</li>
    <li>Delivered within 8 days</li>
    <li>Detailed Submission Report</li>
  </ul>
  <p class="note">Known locally as "SoMa", this neighborhood was home to the dot.com boom and boasts.</p>
</div>
<div class="abs plan orange" style="left:461px">
  <div class="plan-head"><h4>SILVER</h4><em>Great for small business</em></div>
  <div class="plan-price"><span class="amt"><sup>$</sup>58</span><span class="join">JOIN</span></div>
  <ul>
    <li>10 PR3 - PR8 Social Bookmarks</li>
    <li>15 PR5 - PR8 Web 2.0 Profile Backlinks</li>
    <li>100 .EDU Backlinks</li>
    <li>150 PR5 - PR7 Backlinks</li>
    <li>One-Way Links</li>
    <li>Delivered within 8 days</li>
    <li>Detailed Submission Report</li>
  </ul>
  <p class="note">Known locally as "SoMa", this neighborhood was home to the dot.com boom and boasts.</p>
</div>
<div class="abs plan green" style="left:705px">
  <div class="plan-head"><h4>GOLD</h4><em>Great for small business</em></div>
  <div class="plan-price"><span class="amt"><sup>$</sup>79</span><span class="join">JOIN</span></div>
  <ul>
    <li>5 PR4 - PR7 Link Wheels</li>
    <li>15 PR5 - PR8 Web 2.0 Profile Backlinks</li>
    <li>10 PR3 - PR8 Social Bookmarks</li>
    <li>5TB Bandwidth</li>
    <li>One-Way Links</li>
    <li>Delivered within 8 days</li>
    <li>Detailed Submission Report</li>
  </ul>
  <p class="note">Known locally as "SoMa", this neighborhood was home to the dot.com boom and boasts.</p>
</div>

<!-- contact -->
<section class="abs box" style="top:1959px;height:334px"></section>
<h2 class="abs sec-title" style="left:199px;top:1999px;font-weight:400">Get In Touch</h2>
<div class="abs sec-rule" style="left:199px;top:2031px;width:852px;background:#e6e6e6"></div>
<div class="abs label" style="left:216px;top:2050px">Name <i>*</i></div>
<div class="abs label" style="left:447px;top:2050px">E-mail (will not be published) <i>*</i></div>
<div class="abs field" style="left:216px;top:2072px;width:212px;height:25px"></div>
<div class="abs field" style="left:447px;top:2072px;width:212px;height:25px"></div>
<div class="abs label" style="left:216px;top:2108px">Your Message <i>*</i></div>
<div class="abs field" style="left:216px;top:2129px;width:673px;height:95px"></div>
<div class="abs btn" style="left:216px;top:2243px;width:86px">Send E-mail</div>
<div class="abs up" style="left:1143px;top:2155px"></div>

<!-- footer -->
<footer class="abs footer"></footer>
<div class="abs footer-brand">
  <div class="name">RankLoft</div>
  <div class="tag">24/7 Global Support</div>
  <p>Scripta appellantur ullamcorper ut sit, ei vis adhuc causa oporr. Ex est elitr indoctum eu.</p>
</div>
<div class="abs fcol" style="left:378px">
  <h5>Newsletter</h5>
  <p>Subscribe to our newsletter and get latest news and exclusive offers straight to your inbox.</p>
  <div class="sub"><span>Subscribe...</span><b>GO</b></div>
  <p class="fine">No spam, we promise. For more info read<br><a href="#">PRIVACY POLICY.</a></p>
</div>
<div class="abs fcol" style="left:610px">
  <h5>Reelcast</h5>
  <div class="video" role="img" aria-label="Embedded video placeholder"></div>
  <p class="fine" style="margin-top:10px">Pro probo habes debitis ei, ei dicit malo ponderum eos, ei forensibus</p>
</div>
<div class="abs fcol" style="left:841px">
  <h5>News</h5>
  <p>Just over 200 copies sold of Combline HTML <a href="#">lorem ipsum dlorem..</a> New theme coming sooooon!</p>
  <p style="margin-top:14px">Everyone is talking about a hot new app called LUMEN. I went to download it, and it turns out I already have it installed!</p>
</div>
<div class="abs up" style="left:1143px;top:2602px"></div>
<div class="abs bottom">
  <span>© 2014 RankLoft</span>
  <span style="margin-left:262px">TERMS OF USE &nbsp;|&nbsp; PRIVACY POLICY</span>
  <div class="social" style="margin-left:auto;gap:12px"><span></span><span></span><span></span><span></span><span></span><span></span><span></span><span></span></div>
</div>

</body>
</html>
```